The billboard should communicate confidence, energy and approachability while maintaining a professional, premium feel. Rather than relying on a standard agent photograph, property collage or crowded list of services, we would like an original creative idea that makes people look twice. This could involve a fun visual, clever headline, striking colour contrast or an unexpected real estate theme. The concept should feel positive and contemporary, with enough personality to become recognisable throughout the local community.

The key message should appeal to homeowners who are thinking about selling, preparing to sell or simply curious about the value of their property. Copy must be short, clear and conversational, supported by a direct call to action. The agent’s name, phone number and company branding should remain highly visible without competing with the main idea.

The finished billboard will measure 8.0 metres wide by 2.08 metres high (1224px x 324px), so the composition must suit a long landscape format. All important text and imagery should remain comfortably within safe margins and be legible from a distance. The design should avoid small writing, unnecessary detail and visual clutter.

The goal is to create a billboard that feels different from every other real estate sign in the area—something engaging, confident and easy to remember. It should build strong brand awareness, generate conversations and encourage local property owners to contact the agent when they are ready to make their next move. The concept should be adaptable for future campaigns, helping establish a consistent, distinctive and trusted local brand presence.

Target Market(s)

ages 30+

Industry/Entity Type

Real Estate

Requirements
Must have
• call Colin and phone number 0437 15 82 63
Nice to have
• Nice bright and yellow.. Exciting and grabbing

```html
<!DOCTYPE html>
<html lang="en">
<head>
<meta charset="utf-8">
<title>What's Your Home Worth – Dale Forsyth</title>
<link rel="stylesheet" href="https://fonts.googleapis.com/css2?family=Anton&family=Oswald:wght@700&family=Poppins:wght@700&family=Kalam:wght@400&display=swap">
<style>
  :root {
    --yellow: #ffe512;
    --ink: #333333;
    --brand-grey: #555555;
    --white: #ffffff;
    --mark-dark: #111111;
    --mark-mid: #2c2c2c;
  }
  html, body {
    margin: 0;
    padding: 0;
    overflow: hidden;
    background: var(--white);
  }
  .billboard {
    position: relative;
    width: 1200px;
    height: 312px;
    overflow: hidden;
    background: var(--white);
  }
  .billboard__bg {
    position: absolute;
    inset: 0;
  }
  .headline {
    position: absolute;
    left: 37px;
    top: 12px;
    margin: 0;
    font-family: "Anton", Impact, sans-serif;
    font-weight: 400;
    font-size: 110px;
    line-height: 86px;
    color: var(--ink);
    text-transform: uppercase;
    white-space: nowrap;
    letter-spacing: 0.5px;
    transform: scaleY(1.2);
    transform-origin: top left;
  }
  .headline__line {
    display: block;
  }
  .tagline {
    position: absolute;
    left: 106px;
    top: 232px;
    margin: 0;
    color: var(--ink);
    white-space: nowrap;
    line-height: 60px;
  }
  .tagline__curious {
    font-family: "Kalam", cursive;
    font-size: 48px;
  }
  .tagline__action {
    font-family: "Poppins", sans-serif;
    font-weight: 700;
    font-size: 33px;
    margin-left: 6px;
  }
  .question-mark {
    position: absolute;
    left: 664px;
    top: 10px;
    width: 182px;
    height: 280px;
    border-radius: 90px 90px 60px 60px;
    background: radial-gradient(circle at 35% 25%, var(--mark-mid), var(--mark-dark) 70%);
    box-shadow: 6px 4px 0 var(--yellow);
  }
  .contact {
    position: absolute;
    left: 879px;
    top: 108px;
    color: var(--ink);
    font-family: "Oswald", sans-serif;
    font-weight: 700;
    text-transform: uppercase;
    white-space: nowrap;
  }
  .contact__lead {
    margin: 0;
    font-size: 32px;
    line-height: 40px;
  }
  .contact__phone {
    margin: 0;
    font-size: 47px;
    line-height: 56px;
    letter-spacing: 0.5px;
  }
  .brand {
    position: absolute;
    left: 880px;
    top: 226px;
    margin: 0;
    font-family: "Poppins", sans-serif;
    font-weight: 700;
    font-size: 40px;
    line-height: 60px;
    color: var(--brand-grey);
    white-space: nowrap;
  }
</style>
</head>
<body>
  <main class="billboard">
    <svg class="billboard__bg" width="1200" height="312" viewBox="0 0 1200 312" aria-hidden="true">
      <polygon points="0,0 797,0 652,312 0,312" fill="var(--yellow)"/>
      <polygon points="853,217 1200,217 1200,294 827,294" fill="var(--yellow)"/>
    </svg>

    <h1 class="headline">
      <span class="headline__line">What’s Your</span>
      <span class="headline__line">Home Worth</span>
    </h1>

    <p class="tagline">
      <span class="tagline__curious">Curious?</span><span class="tagline__action">Let’s find out.</span>
    </p>

    <div class="question-mark" role="img" aria-label="Large glossy black 3D question mark with a yellow edge"></div>

    <div class="contact">
      <p class="contact__lead">Talk to Colin</p>
      <p class="contact__phone">0437 15 82 63</p>
    </div>

    <p class="brand">Dale Forsyth</p>
  </main>
</body>
</html>
```